Business Card Design Project

Hi,

We are a new modern sheet metal business and I require a business card for our sales reps.

The card should be double sided and standout in a crowd.

I have attached our logo and our website is www.folvik.com.au.

Please ask if you have any further questions
Updates

hi everyone, 

I'm wondering if we can try to lighten the cards mood.  Everyone is using black and I'm not sure how that would be accepted in real life.

Gregory

Reason: Still No receiving what I was hoping for.

Industry/Entity Type

Business

Requirements
Must have
• double sided

```html
<!DOCTYPE html>
<html lang="en">
<head>
<meta charset="utf-8">
<title>Folvik Sheetmetal – Business Card</title>
<link rel="stylesheet" href="https://fonts.googleapis.com/css2?family=Jost:ital,wght@0,400;0,500;0,700;1,400&display=swap">
<style>
  :root {
    --navy: #233a7a;
    --grey-text: #6b6b6b;
    --backdrop: #c9cacc;
    --card: #ffffff;
    --metal-light: #e4e6ea;
    --metal-mid: #c2c6cd;
    --metal-dark: #a9adb5;
    --mark-faint: #9a9ea6;
  }
  * { margin: 0; padding: 0; box-sizing: border-box; }
  html, body {
    width: 1200px;
    height: 787px;
    overflow: hidden;
  }
  body {
    position: relative;
    background: var(--backdrop);
    font-family: "Jost", "Futura", sans-serif;
    color: var(--navy);
  }

  /* ---------- Brand side ---------- */
  .card-brand {
    position: absolute;
    left: 600px;
    top: 30px;
    width: 540px;
    height: 330px;
    background: var(--card);
    display: flex;
    flex-direction: column;
    align-items: center;
    justify-content: center;
  }
  .brand-name {
    font-weight: 700;
    color: var(--navy);
    text-align: center;
    line-height: 1;
  }
  .brand-name .brand-word {
    display: block;
    font-size: 96px;
    letter-spacing: 2px;
  }
  .brand-name .brand-trade {
    display: block;
    font-size: 27px;
    letter-spacing: 9px;
    margin-top: 8px;
    padding-left: 9px;
  }
  .services {
    margin-top: 26px;
    display: flex;
    align-items: center;
    gap: 10px;
    font-size: 19px;
    color: var(--grey-text);
  }
  .services .divider {
    width: 3px;
    height: 20px;
    background: var(--navy);
  }

  /* ---------- Contact side ---------- */
  .card-contact {
    position: absolute;
    left: 115px;
    top: 372px;
    width: 553px;
    height: 345px;
    background: var(--card);
    display: flex;
  }
  .metal-panel {
    position: relative;
    width: 190px;
    height: 100%;
    background: linear-gradient(180deg, var(--metal-mid) 0%, var(--metal-light) 45%, var(--metal-mid) 75%, var(--metal-dark) 100%);
  }
  .metal-panel .panel-texture {
    position: absolute;
    inset: 0;
  }
  .panel-mark {
    position: absolute;
    left: 28px;
    top: 246px;
    font-weight: 700;
    font-size: 40px;
    letter-spacing: 1px;
    color: var(--mark-faint);
  }
  .accent-rule {
    width: 5px;
    height: 100%;
    background: var(--navy);
  }
  .contact-details {
    padding: 64px 0 0 21px;
  }
  .rep-name {
    font-weight: 700;
    font-size: 21px;
    line-height: 1.1;
  }
  .rep-title {
    font-style: italic;
    font-size: 16px;
    margin-top: 2px;
  }
  .numbers {
    margin-top: 24px;
    display: grid;
    grid-template-columns: 88px auto;
    font-size: 19px;
    line-height: 24px;
  }
  .addresses {
    margin-top: 17px;
    font-size: 17px;
    line-height: 26px;
  }
</style>
</head>
<body>

  <section class="card-brand" aria-label="Card front">
    <div class="brand-name">
      <span class="brand-word">FOLVIK</span>
      <span class="brand-trade">SHEETMETAL</span>
    </div>
    <div class="services">
      <span>Flashings</span>
      <span class="divider"></span>
      <span>Gutter</span>
      <span class="divider"></span>
      <span>Rainwater Goods</span>
    </div>
  </section>

  <section class="card-contact" aria-label="Card back">
    <div class="metal-panel">
      <svg class="panel-texture" width="190" height="345" role="img" aria-label="Brushed steel texture panel">
        <rect width="190" height="345" fill="none"/>
      </svg>
      <span class="panel-mark">FOLVIK</span>
    </div>
    <div class="accent-rule"></div>
    <div class="contact-details">
      <h1 class="rep-name">Gregory Hale</h1>
      <p class="rep-title">Sales Representative</p>
      <div class="numbers">
        <span>Mobile</span><span>: 561 902 3317</span>
        <span>Phone</span><span>: 3604 2215</span>
        <span>Fax</span><span>: 3604 2290</span>
      </div>
      <div class="addresses">
        <p>28 Quartz Road Linden Vale Q 4410</p>
        <p>PO Box 587 Linden Vale Q 4410</p>
      </div>
    </div>
  </section>

</body>
</html>
```